Presentation Folder

Design presentation folder for professional law firm. Our law firm primarily represents individuals who are dealing with divorce, child custody, child support, spousal support, wills, estates and other civil litigation.
We desire a simple, professional, but memorable presentation folder that we can give clients containing their important documents (e.g., contract, and other important papers). The folder will also have a place for a business card. We will print this at Prindlebay. Specs and Templates are available at http://www.prindlebay-example.com/vp/ns/propath/UploadResources.aspx?selectedTab=0?pfid=156&pf_id=156&xnav=studio-side-bar#Templates
Our logo and one of our business cards is attached.
Our website is www.HolloweyFamilyLaw-example.com
Target Market(s)
Individual with legal issues primarily undergoing divorce
Industry/Entity Type
Law Firm
Font styles to use
Other font styles liked:
- Tahoma
Look and feel

```html
<!DOCTYPE html>
<html lang="en">
<head>
<meta charset="utf-8">
<title>Hollowey Law PLLC – Presentation Folder, Back Cover</title>
<link rel="stylesheet" href="https://fonts.googleapis.com/css2?family=Arimo:wght@700&family=Tinos:wght@700&display=swap">
<style>
  :root {
    --backdrop: #efe9df;
    --navy-deep: #1c2453;
    --navy: #28305e;
    --gold: #d4a020;
    --gold-line: #d9a826;
  }
  * { box-sizing: border-box; margin: 0; padding: 0; }
  html, body {
    width: 1200px;
    height: 800px;
    overflow: hidden;
  }
  body {
    background: var(--backdrop);
    display: flex;
    align-items: center;
    justify-content: center;
  }
  .folder-back {
    position: relative;
    width: 450px;
    height: 600px;
    background: linear-gradient(160deg, var(--navy-deep) 0%, var(--navy) 100%);
    box-shadow: 0 6px 18px rgba(40, 30, 10, 0.25);
  }
  .firm-mark {
    position: absolute;
    left: 50%;
    top: 318px;
    transform: translate(-50%, -50%);
    display: flex;
    align-items: center;
    gap: 8px;
    white-space: nowrap;
  }
  .firm-mark__square {
    width: 14px;
    height: 14px;
    background: var(--gold);
  }
  .firm-mark__name {
    font-family: "Tinos", "Times New Roman", serif;
    font-weight: 700;
    font-size: 24px;
    letter-spacing: 2px;
    color: var(--gold);
  }
  .contact {
    position: absolute;
    left: 62px;
    top: 382px;
    color: var(--gold);
    line-height: 21px;
  }
  .contact__web {
    font-family: "Tinos", "Times New Roman", serif;
    font-weight: 700;
    font-size: 12.5px;
    letter-spacing: 2.4px;
    text-transform: uppercase;
  }
  .contact__line {
    font-family: "Tinos", "Times New Roman", serif;
    font-weight: 700;
    font-size: 14px;
    letter-spacing: 1px;
  }
  .contact__number {
    font-family: "Arimo", Arial, sans-serif;
    font-weight: 700;
    letter-spacing: 1.2px;
  }
  .gold-rule {
    position: absolute;
    left: 0;
    right: 0;
    top: 500px;
    height: 4px;
    background: var(--gold-line);
  }
</style>
</head>
<body>
  <main class="folder-back">
    <div class="firm-mark">
      <span class="firm-mark__square"></span>
      <span class="firm-mark__name">HOLLOWEY LAW PLLC</span>
    </div>
    <div class="contact">
      <p class="contact__web">www.HolloweyFamilyLaw-example.com</p>
      <p class="contact__line">Telephone: <span class="contact__number">(555) 014-2876</span></p>
      <p class="contact__line">Facsimile: <span class="contact__number">(555) 014-3907</span></p>
    </div>
    <div class="gold-rule"></div>
  </main>
</body>
</html>
```